Indian Takeaway Menu -

I would like to have double parallel fold A4 sheet menu.
A4 sheet cut in half and attached to the other half to make the sheet 4 small pages long.

Colors
abd036
ffffff

Requirements
Must have
• Please check new attachments - menu size and layout is not correct.
• I would like to add Dark brown colour. A4 sheet folded 4x Menu layout pocket size.
Nice to have
• Dark Brown - Parrot Green and very light Brown

```html
<!DOCTYPE html>
<html lang="en">
<head>
<meta charset="utf-8">
<title>Healthy Side Orders &amp; Meal Deals</title>
<link href="https://fonts.googleapis.com/css2?family=Roboto+Condensed:wght@400;700&family=Roboto:wght@400;500&display=swap" rel="stylesheet">
<style>
:root{
  --green:#abd036;
  --white:#ffffff;
  --brown:#4a2c1a;
  --brown-soft:#6b4a36;
  --light-brown:#f4ece1;
  --red:#d42a2f;
  --dots:#a89484;
  --curry:#c4502a;
}
*{box-sizing:border-box;margin:0;padding:0}
html,body{width:934px;height:1200px;overflow:hidden;background:var(--white)}
body{position:relative;font-family:'Roboto',sans-serif;color:var(--brown)}
.abs{position:absolute}
.band{position:absolute;background:var(--green);color:var(--white);font-family:'Roboto Condensed',sans-serif;font-weight:700}
.band-sides{left:12px;top:26px;width:906px;height:36px;font-size:23px;padding:4px 0 0 16px}
.band-deals{left:11px;top:472px;width:909px;height:35px;font-size:24px;padding:3px 0 0 15px}
.band-deals small{font-size:17px;font-weight:400}
.side{position:absolute;width:316px}
.side-name{position:relative;font-family:'Roboto Condensed',sans-serif;font-size:18px;height:22px}
.side-name .tag{position:absolute;left:154px;font-size:16px}
.side-name .price{position:absolute;right:0;font-size:18px}
.side-desc{font-size:11.2px;line-height:15px;color:var(--brown-soft);margin-top:3px;width:212px}
.rule{position:absolute;height:0;border-top:2px dotted var(--dots)}
.legend{position:absolute;left:438px;top:330px;width:326px;height:62px;border:1.5px solid var(--green);background:#fbfcf2;font-family:'Roboto Condensed',sans-serif;font-weight:700;font-size:11px}
.legend span{position:absolute}
.choose{left:26px;top:517px;font-family:'Roboto Condensed',sans-serif;font-size:13px}
.deal{position:absolute;left:26px;width:370px;height:70px}
.deal-photo{position:absolute;left:0;top:0;width:89px;height:70px;background:linear-gradient(135deg,#d96b33,var(--curry) 55%,#7a2a15)}
.badge{position:absolute;left:72px;top:18px;width:34px;height:34px;border-radius:50%;background:var(--red);color:var(--white);font-family:'Roboto Condensed',sans-serif;font-weight:700;font-size:13px;line-height:34px;text-align:center}
.deal-name{position:absolute;left:110px;top:-2px;font-family:'Roboto Condensed',sans-serif;font-weight:700;font-size:18px}
.deal-desc{position:absolute;left:110px;top:23px;width:240px;font-size:11.2px;line-height:15px;color:var(--brown-soft)}
.vdots{position:absolute;width:0;border-left:3px dotted var(--dots)}
.set{position:absolute}
.set h3{font-family:'Roboto Condensed',sans-serif;font-weight:700;font-size:18px;margin-bottom:7px}
.set li{list-style:none;font-family:'Roboto Condensed',sans-serif;font-size:11.5px;height:20.8px;display:flex;align-items:center;gap:6px}
.set li svg{width:10px;height:8px}
.footer{position:absolute;left:0;top:944px;width:934px;height:205px;background:var(--light-brown)}
.allergens{position:absolute;font-family:'Roboto Condensed',sans-serif;font-size:18.5px;line-height:29.6px}
.contact-head{position:absolute;font-family:'Roboto Condensed',sans-serif;font-weight:700;font-size:23px;color:var(--green);display:flex;align-items:center;gap:6px}
.contact-text{position:absolute;font-family:'Roboto Condensed',sans-serif;font-size:16px;line-height:26.5px}
.delivery{position:absolute;left:442px;top:1066px;width:281px;height:49px;border-radius:25px;background:var(--green);font-family:'Roboto Condensed',sans-serif;font-weight:700;font-size:19px;text-align:center;line-height:49px;color:var(--brown)}
.note{position:absolute;left:738px;top:1070px;font-family:'Roboto Condensed',sans-serif;font-size:18px;line-height:20px}
.band-bottom{position:absolute;left:13px;top:1144px;width:907px;height:42px;background:var(--green)}
.web{position:absolute;left:329px;top:1132px;width:278px;height:38px;background:var(--white);border-radius:0 0 20px 20px;text-align:center;font-family:'Roboto Condensed',sans-serif;font-size:17px;line-height:36px;color:var(--brown)}
.fold{position:absolute;width:8px;height:0;border-top:1px solid var(--brown)}
</style>
</head>
<body>
<svg width="0" height="0" class="abs" aria-hidden="true">
  <symbol id="tick" viewBox="0 0 10 8"><path d="M1 4l3 3 5-6" fill="none" stroke="#8a7566" stroke-width="1.8"/></symbol>
</svg>

<div class="fold" style="left:0;top:300px"></div><div class="fold" style="right:0;top:300px"></div>
<div class="fold" style="left:0;top:600px"></div><div class="fold" style="right:0;top:600px"></div>
<div class="fold" style="left:0;top:900px"></div><div class="fold" style="right:0;top:900px"></div>

<header class="band band-sides">Healthy&nbsp; Side orders</header>

<div class="side" style="left:26px;top:84px"><div class="side-name">Sautéed Broccoli<span class="tag">v</span><span class="price">5.00</span></div><p class="side-desc">Broccoli, green beans and spinach leaves sautéed with roasted cumin and fresh garlic.</p></div>
<div class="side" style="left:26px;top:170px"><div class="side-name">Chana Saag&nbsp;&nbsp; 3<span class="tag">y v</span><span class="price">5.00</span></div><p class="side-desc">Chickpeas cooked with chopped spinach, onion, and cumin and finished with cream.</p></div>
<div class="side" style="left:26px;top:257px"><div class="side-name">Chana Masala<span class="tag" style="left:152px">v</span><span class="price">5.00</span></div><p class="side-desc">Chickpeas simmered with tomato, caramelised onion, black pepper and fresh coriander.</p></div>
<div class="side" style="left:26px;top:343px"><div class="side-name">Aloo Saag&nbsp;&nbsp; 3<span class="tag">y v</span><span class="price">5.00</span></div><p class="side-desc">Crispy Potato with spinach, caramelised onion, garam&nbsp; masala and a dash of cream.</p></div>

<div class="side" style="left:438px;top:84px"><div class="side-name">Aloo Ghobhi<span class="tag" style="left:160px">v</span><span class="price">5.00</span></div><p class="side-desc" style="width:215px">Crispy Potatoes cubes &amp; Cauliflower cooked with roasted cumin with tomato and onion gravy.</p></div>
<div class="side" style="left:438px;top:170px"><div class="side-name">Tarka Daal&nbsp;&nbsp;&nbsp; 4<span class="tag" style="left:153px">y v</span><span class="price">5.00</span></div><p class="side-desc" style="width:215px">Home style soaked yellow chana cooked with cumin &amp; garam masala</p></div>
<div class="side" style="left:438px;top:257px"><div class="side-name">Tangy&nbsp; Aloo<span class="tag" style="left:155px">v</span><span class="price">5.00</span></div><p class="side-desc" style="width:205px">Crispy Potatoes cubes cooked with roasted cumin and touch of our tangy sauce</p></div>

<div class="rule" style="left:27px;top:160px;width:313px"></div>
<div class="rule" style="left:27px;top:249px;width:313px"></div>
<div class="rule" style="left:27px;top:335px;width:313px"></div>
<div class="rule" style="left:439px;top:160px;width:313px"></div>
<div class="rule" style="left:439px;top:249px;width:313px"></div>

<div class="legend">
  <span style="left:16px;top:14px">Y: can be cooked without allergen</span>
  <span style="left:199px;top:14px">H: Healthy Option</span>
  <span style="left:16px;top:37px">V: Suitable for Vegans</span>
</div>

<header class="band band-deals">Meal Deals only €8.50 <small>(Low Fat Dishes)</small></header>
<p class="abs choose">Choose with Rice or Plain Naan</p>

<div class="deal" style="top:556px"><div class="deal-photo" role="img" aria-label="Photo of chicken dupiaza curry"></div><div class="badge">8.5$</div><h4 class="deal-name">Chicken Dupiaza</h4><p class="deal-desc">Chicken cooked with ginger and chunks of onions and finished with onion seeds</p></div>
<div class="rule" style="left:140px;top:630px;width:253px"></div>
<div class="deal" style="top:647px"><div class="deal-photo" role="img" aria-label="Photo of chicken rogan josh"></div><div class="badge">8.5$</div><h4 class="deal-name">Chicken Rogan josh</h4><p class="deal-desc">A red chicken curry prepared with fresh herb &amp; spices, a delicacy from Kashmir</p></div>
<div class="rule" style="left:140px;top:725px;width:253px"></div>
<div class="deal" style="top:736px"><div class="deal-photo" role="img" aria-label="Photo of chicken bhuna"></div><div class="badge">8.5$</div><h4 class="deal-name">Chicken Bhuna</h4><p class="deal-desc">Tomatoes and onion sauce cooked with black peppers &amp; spring onions</p></div>
<div class="rule" style="left:140px;top:811px;width:253px"></div>
<div class="deal" style="top:825px"><div class="deal-photo" role="img" aria-label="Photo of tarkari makhani vegetable curry"></div><div class="badge">8.5$</div><h4 class="deal-name">Tarkari Makhani</h4><p class="deal-desc">Mixed seasonal vegetables in a smooth tikka masala sauce</p></div>

<div class="vdots" style="left:408px;top:552px;height:334px"></div>
<div class="vdots" style="left:680px;top:552px;height:334px"></div>

<div class="set" style="left:442px;top:550px"><h3>Set Meal 1 .........€16.00</h3><ul>
<li><svg><use href="#tick"/></svg>Onion bhajia</li><li><svg><use href="#tick"/></svg>Chicken Tikka Masala</li><li><svg><use href="#tick"/></svg>Pilau rice</li><li><svg><use href="#tick"/></svg>Naan</li><li><svg><use href="#tick"/></svg>Poppadoms</li></ul></div>
<div class="set" style="left:442px;top:710px"><h3>Set Meal 2 .........€27.00</h3><ul>
<li><svg><use href="#tick"/></svg>Onion bhajia</li><li><svg><use href="#tick"/></svg>Chicken tikka</li><li><svg><use href="#tick"/></svg>Chicken Tikka Masala</li><li><svg><use href="#tick"/></svg>Lamb Roganjosh</li><li><svg><use href="#tick"/></svg>2xPilau rice</li><li><svg><use href="#tick"/></svg>1xNaan</li><li><svg><use href="#tick"/></svg>Poppadom</li></ul></div>
<div class="set" style="left:705px;top:550px"><h3>Set Meal 3/4 .........€43.00</h3><ul>
<li><svg><use href="#tick"/></svg>Onion bhajia</li><li><svg><use href="#tick"/></svg>Vegetable samosa</li><li><svg><use href="#tick"/></svg>Chicken tikka</li><li><svg><use href="#tick"/></svg>Chicken Tikka Masala</li><li><svg><use href="#tick"/></svg>Lamb Roganjosh</li><li><svg><use href="#tick"/></svg>Sambhar Veg Curry</li><li><svg><use href="#tick"/></svg>2 x Pilau Rice</li><li><svg><use href="#tick"/></svg>2 x Naan</li><li><svg><use href="#tick"/></svg>Poppadom</li></ul></div>

<footer class="footer"></footer>
<div class="allergens" style="left:54px;top:970px">1 celery ,<br>2 gluten ,<br>3 dairy ,<br>4 mustard,<br>5 nuts,</div>
<div class="allergens" style="left:160px;top:970px">6 egg,<br>7 fish,<br>8 soya,<br>9 penuts,<br>10 lupin,</div>
<div class="allergens" style="left:246px;top:970px">11 sulpher dioxide,<br>12 sesame seeds,<br>13 molluscs,<br>14 crustanceans</div>
<div class="vdots" style="left:416px;top:974px;height:138px;border-left-width:2px"></div>

<div class="contact-head" style="left:444px;top:968px"><svg width="18" height="18" viewBox="0 0 24 24"><path fill="#abd036" d="M6.6 10.8a15.1 15.1 0 006.6 6.6l2.2-2.2c.3-.3.7-.4 1-.2 1.1.4 2.3.6 3.6.6.6 0 1 .4 1 1V20c0 .6-.4 1-1 1A17 17 0 013 4c0-.6.4-1 1-1h3.5c.6 0 1 .4 1 1 0 1.3.2 2.5.6 3.6.1.3 0 .7-.2 1z"/></svg>PHONE</div>
<div class="contact-text" style="left:469px;top:1002px">+ 015550127,<br>+ 015550129</div>
<div class="contact-head" style="left:600px;top:968px"><svg width="22" height="22" viewBox="0 0 24 24" fill="none" stroke="#abd036" stroke-width="2.2"><path d="M4 12a8 8 0 108-8 8 8 0 00-6.5 3.3"/><path d="M4 4v4h4"/><path d="M12 8v4l3 2"/></svg>OPENING HOURS:</div>
<div class="contact-text" style="left:631px;top:1002px">Sun - Thurs 5PM to 10.00PM<br>Fri &nbsp;&nbsp;- Sat &nbsp;&nbsp;&nbsp;5.00PM-10.30PM</div>

<div class="delivery">Deliveries From 5.30PM</div>
<p class="note">All our meals are<br>cooked to order.</p>

<div class="band-bottom"></div>
<div class="web">www.saffronhouse.ie</div>
</body>
</html>
```